Large multi-office optometry business opening a Dry Eye Spa and needs sign.

Business name/sign info: Brindlecove Dry Eye Institute, (555) 316-4872
Backlit pole sign at office entrance on a very busy street
Sign dimensions: 53" tall x 136.5" wide
State of the art Dry Eye Spa for treatment of all forms of dry eye and ocular surface disease. Also, have aesthetics treatments (IPL, Low Level Light Treatment, etc.)

Target Market(s)

People who are suffering from: dryness, burning, foreign body sensation, itching, fluctuating vision, tired eyes, etc.

Industry/Entity Type

Optometry and aesthetics

Colors
0054AA
0677BA
7BADD7
CADEEF
E8F1F8

Requirements
Must have
• Business name, phone number, subliminal message of relief in a glance or short look.
Nice to have
• Cool, relief, soothing sense.
Should not have
• Too much information or too busy.

```html
<!DOCTYPE html>
<html lang="en">
<head>
<meta charset="utf-8">
<title>Brindlecove Dry Eye Institute – Pole Sign</title>
<link href="https://fonts.googleapis.com/css2?family=Crimson+Pro:wght@600&family=Montserrat:wght@600&display=swap" rel="stylesheet">
<style>
  :root {
    --page: #ffffff;
    --sign-face: #ffffff;
    --navy: #1f4477;
    --mark-blue: #7badd7;
    --phone-text: #ffffff;
  }
  * { margin: 0; padding: 0; box-sizing: border-box; }
  html, body {
    width: 1200px;
    height: 1200px;
    overflow: hidden;
    background: var(--page);
  }
  .sign {
    position: absolute;
    left: 79px;
    top: 397px;
    width: 1042px;
    height: 405px;
    background: var(--sign-face);
    box-shadow: 0 0 40px rgba(0, 0, 0, 0.18);
    overflow: hidden;
  }
  .sign__band {
    position: absolute;
    inset: 0;
    width: 100%;
    height: 100%;
  }
  .sign__mark {
    position: absolute;
    left: 112px;
    top: 92px;
    width: 170px;
    height: 170px;
  }
  .sign__name {
    position: absolute;
    left: 370px;
    width: 600px;
    top: 30px;
    text-align: center;
    font-family: "Crimson Pro", Georgia, serif;
    font-weight: 600;
    color: var(--navy);
    line-height: 1;
    text-transform: uppercase;
  }
  .sign__name-top {
    display: block;
    font-size: 44px;
    letter-spacing: 6px;
  }
  .sign__name-main {
    display: block;
    font-size: 124px;
    letter-spacing: 1px;
    margin-top: -4px;
  }
  .sign__name-bottom {
    display: block;
    font-size: 66px;
    letter-spacing: 6px;
    margin-top: -10px;
  }
  .sign__phone {
    position: absolute;
    right: 37px;
    top: 318px;
    font-family: "Montserrat", Arial, sans-serif;
    font-weight: 600;
    font-size: 59px;
    line-height: 1;
    color: var(--phone-text);
  }
</style>
</head>
<body>
  <div class="sign">
    <svg class="sign__band" viewBox="0 0 1042 405" preserveAspectRatio="none" aria-hidden="true">
      <path d="M0 303 C80 340 150 358 240 356 C340 354 400 325 505 295 C560 282 600 292 640 292 L1042 291 L1042 405 L0 405 Z" fill="var(--navy)"/>
    </svg>
    <svg class="sign__mark" viewBox="0 0 170 170" aria-hidden="true">
      <circle cx="85" cy="85" r="85" fill="var(--mark-blue)"/>
    </svg>
    <h1 class="sign__name">
      <span class="sign__name-top">Brindlecove</span>
      <span class="sign__name-main">Dry Eye</span>
      <span class="sign__name-bottom">Institute</span>
    </h1>
    <p class="sign__phone">555-316-4872</p>
  </div>
</body>
</html>
```